New Business Card for General Contractor Marketing

Need a business card the is more like a marketing promotion of our services
Must be horizontal orientation, One Sided Only, Max font size, Organize the Services
#1 General Contractor for Realtors
Remodels – Renovations – Repairs
Water & Mold Damage Experts
Painting: Interior/ Exterior
Flooring: Wood / LVT / Carpet
Plumbing: Repairs & Upgrades
Electric: Lights & Energy Efficient Upgrades
Kitchen & Bath Remodels
Fast Inspections Repair Billed Thru Escrow
BrightHarborBuilds.com
555-418-2796

Industry/Entity Type

General Contractor

Contact Information for Business Card

One Sided Only: #1 General Contractor for Realtors Remodels – Renovations – Repairs Water & Mold Damage Experts Painting: Interior/ Exterior Flooring: Wood / LVT / Carpet Plumbing: Repairs & Upgrades Electric: Lights & Energy Efficient Upgrades Kitchen & Bath Remodels Fast Inspections Repair Billed Thru Escrow BrightHarborBuilds.com 555-418-2796

Colors
0054AA
0677BA
7BADD7
CADEEF
E8F1F8

Requirements
Must have
• One Sided Only: #1 General Contractor for Realtors Remodels – Renovations – Repairs Water & Mold Damage Experts Painting: Interior/ Exterior Flooring: Wood / LVT / Carpet Plumbing: Repairs & Upgrades Electric: Lights & Energy Efficient Upgrades Kitchen & Bath Remodels Fast Inspections Repair Billed Thru Escrow BrightHarborBuilds.com 555-418-2796

```html
<!DOCTYPE html>
<html lang="en">
<head>
<meta charset="utf-8">
<title>Bright Harbor Builds – Business Card</title>
<link rel="stylesheet" href="https://fonts.googleapis.com/css2?family=Arimo:wght@400;700&family=Tinos:wght@400;700&display=swap">
<style>
  :root {
    --page-bg: #e8e5e0;
    --blue-light: #0c54a8;
    --blue-dark: #142f6b;
    --blue-brand: #1c3f8c;
    --orange: #ef7f1a;
    --silver: #c9ccd2;
    --white: #ffffff;
  }
  * { box-sizing: border-box; margin: 0; padding: 0; }
  html, body {
    width: 1200px; height: 900px; overflow: hidden;
    background: var(--page-bg);
  }
  .card {
    position: absolute; left: 75px; top: 150px;
    width: 1050px; height: 600px;
    background: radial-gradient(ellipse at 40% 25%, var(--blue-light) 0%, var(--blue-dark) 85%);
    box-shadow: 0 18px 40px rgba(0,0,0,0.25);
    overflow: hidden;
  }
  .card-swoosh { position: absolute; inset: 0; width: 1050px; height: 600px; }
  .services {
    position: absolute; left: 60px; top: 110px;
    font-family: "Arimo", Arial, sans-serif; color: var(--white);
  }
  .services-title {
    font-family: "Tinos", "Times New Roman", serif; font-weight: 700;
    color: var(--orange); font-size: 24px; letter-spacing: 0.5px;
    margin-bottom: 8px;
  }
  .services-list { list-style: none; }
  .services-list li {
    font-size: 22px; line-height: 35px;
    display: flex; align-items: center; gap: 14px;
  }
  .services-list li::before {
    content: ""; width: 11px; height: 11px; background: var(--orange); flex: none;
  }
  .offer {
    position: absolute; right: 60px; top: 58px; text-align: left;
    width: 420px;
  }
  .offer-headline {
    font-family: "Tinos", "Times New Roman", serif; font-weight: 700;
    color: var(--orange); font-size: 52px; line-height: 1;
  }
  .offer-sub {
    font-family: "Tinos", "Times New Roman", serif; font-weight: 700;
    color: var(--orange); font-size: 26px; margin: 6px 0 22px 24px;
  }
  .contact-phone {
    font-family: "Arimo", Arial, sans-serif; color: var(--orange);
    font-size: 44px; display: flex; align-items: center; gap: 10px;
    margin-left: 40px;
  }
  .contact-phone svg { width: 40px; height: 40px; flex: none; }
  .contact-web {
    font-family: "Arimo", Arial, sans-serif; color: var(--white);
    font-size: 29px; margin: 12px 0 0 40px;
  }
  .brand {
    position: absolute; left: 470px; top: 460px; width: 540px;
    text-align: center; font-family: "Tinos", "Times New Roman", serif;
  }
  .brand-name {
    display: inline-flex; align-items: center; gap: 14px;
    color: var(--blue-brand); font-weight: 700; font-size: 38px;
  }
  .brand-name::before {
    content: ""; width: 20px; height: 20px; background: var(--orange);
  }
  .brand-role {
    color: var(--blue-brand); font-size: 21px; letter-spacing: 2px;
    text-transform: uppercase; margin-top: 6px;
  }
  .brand-tagline {
    font-family: "Arimo", Arial, sans-serif; color: var(--orange);
    font-size: 18px; margin-top: 4px;
  }
</style>
</head>
<body>
  <section class="card">
    <svg class="card-swoosh" viewBox="0 0 1050 600" aria-hidden="true">
      <polygon points="0,512 570,362 1050,425 1050,441 570,378 0,530" fill="var(--silver)"/>
      <polygon points="0,530 570,378 1050,441 1050,451 570,388 0,542" fill="var(--orange)"/>
      <polygon points="0,542 570,388 1050,451 1050,600 0,600" fill="var(--white)"/>
    </svg>

    <div class="services">
      <h2 class="services-title">OUR SERVICES</h2>
      <ul class="services-list">
        <li>Water &amp; Mold Damage Experts</li>
        <li>Painting: Interior/ Exterior</li>
        <li>Flooring: Wood / LVT / Carpet</li>
        <li>Plumbing: Repairs &amp; Upgrades</li>
        <li>Electric: Lights &amp; Energy Efficient Upgrades</li>
        <li>Kitchen &amp; Bath Remodels</li>
      </ul>
    </div>

    <div class="offer">
      <h1 class="offer-headline">Fast Inspections</h1>
      <p class="offer-sub">Repair Billed Thru Escrow</p>
      <p class="contact-phone">
        <svg viewBox="0 0 24 24" aria-hidden="true">
          <path fill="var(--orange)" d="M6.6 10.8c1.4 2.8 3.8 5.1 6.6 6.6l2.2-2.2c.3-.3.7-.4 1-.2 1.1.4 2.3.6 3.6.6.6 0 1 .4 1 1V20c0 .6-.4 1-1 1C10.6 21 3 13.4 3 4c0-.6.4-1 1-1h3.5c.6 0 1 .4 1 1 0 1.3.2 2.5.6 3.6.1.3 0 .7-.2 1L6.6 10.8z"/>
          <path fill="none" stroke="var(--orange)" stroke-width="1.8" stroke-linecap="round" d="M14.5 3.5a6.5 6.5 0 0 1 6 6M14.5 7a3 3 0 0 1 2.6 2.6"/>
        </svg>
        555-418-2796
      </p>
      <p class="contact-web">BrightHarborBuilds.com</p>
    </div>

    <div class="brand">
      <p class="brand-name">Bright Harbor Builds</p>
      <p class="brand-role">General Contractor for Realtors</p>
      <p class="brand-tagline">Remodels – Renovations – Repairs</p>
    </div>
  </section>
</body>
</html>
```